Corinne Dabney Interiors business cards

We need a DOUBLE SIDED business card design that is simple, elegant and modern. We are a rapidly growing Interior Design Firm, and our brand colours are blush pink, navy, and antique gold, so we require some or all of these colours to be used. The final design should portray elegance, simplicity, and have a modern feel. We have upload inspiration photos that have the feel we're looking for.

Industry/Entity Type

Interior Design

Contact Information for Business Card

Contact information and LOGO

Colors
EB3D1F
EC4F4E
F09395
F8D3D4
FCEDEE

Requirements
Must have
• Navy, the right shade of blush pink, and antique gold

```html
<!DOCTYPE html>
<html lang="en">
<head>
<meta charset="utf-8">
<title>Corinne Dabney Interiors – Business Cards</title>
<link href="https://fonts.googleapis.com/css2?family=Jost:wght@400&family=Open+Sans:wght@400;700&display=swap" rel="stylesheet">
<style>
  :root {
    --backdrop: #5b5b5b;
    --card-blush: #fcf0f0;
    --panel-blush: #f6dadc;
    --gold-tint: #efd9b8;
    --antique-gold: #c9a13e;
    --navy: #1f2a5c;
  }
  * { margin: 0; padding: 0; box-sizing: border-box; }
  html, body {
    width: 1200px; height: 586px; overflow: hidden;
    background: var(--backdrop);
  }
  .sheet {
    width: 1200px; height: 586px;
    display: flex; align-items: center; justify-content: center; gap: 20px;
  }
  .card {
    position: relative;
    width: 570px; height: 326px;
    background: var(--card-blush);
    overflow: hidden;
  }

  /* Decorative area kept as a soft tonal field */
  .decor-field {
    position: absolute; inset: 0;
    background: linear-gradient(135deg, var(--panel-blush) 0%, var(--card-blush) 45%, var(--gold-tint) 75%, var(--panel-blush) 100%);
  }
  .card-front .decor-field {
    clip-path: polygon(45.6% 0, 100% 0, 100% 100%, 46% 100%, 66% 79%);
  }
  .card-back .decor-field {
    clip-path: polygon(0 0, 55% 0, 33% 80%, 54% 100%, 0 100%);
  }

  /* Front */
  .brand {
    position: absolute; left: 18px; top: 127px; width: 280px;
    display: flex; flex-direction: column; align-items: center; gap: 40px;
  }
  .brand-square {
    width: 46px; height: 46px; background: var(--navy);
  }
  .brand-name {
    font-family: "Jost", sans-serif; font-weight: 400;
    font-size: 14.5px; letter-spacing: 0.01em; line-height: 1;
    color: var(--antique-gold); text-transform: uppercase;
    white-space: nowrap; text-align: center;
  }

  /* Back */
  .holder {
    position: absolute; right: 33px; top: 60px; text-align: right;
    color: var(--navy); font-family: "Open Sans", sans-serif;
  }
  .holder-name { font-size: 25px; line-height: 1; letter-spacing: 0.01em; white-space: nowrap; }
  .holder-name strong { font-weight: 700; }
  .holder-role { font-size: 15.5px; line-height: 1.2; margin-top: 3px; }

  .contact-list {
    position: absolute; right: 33px; top: 145px;
    list-style: none; font-family: "Open Sans", sans-serif;
    font-size: 12px; color: var(--navy);
  }
  .contact-item {
    display: flex; align-items: center; justify-content: flex-end;
    gap: 13px; height: 22px; margin-bottom: 11.5px; white-space: nowrap;
  }
  .contact-icon { width: 22px; height: 22px; flex: none; }
  .contact-icon * { stroke: var(--navy); stroke-width: 1.6; fill: none; stroke-linecap: round; stroke-linejoin: round; }
</style>
</head>
<body>
<main class="sheet">

  <section class="card card-front" aria-label="Card front">
    <div class="decor-field" role="img" aria-label="Decorative geometric pattern of blush facets with antique gold lines"></div>
    <div class="brand">
      <div class="brand-square" aria-hidden="true"></div>
      <p class="brand-name">Corinne Dabney Interiors</p>
    </div>
  </section>

  <section class="card card-back" aria-label="Card back">
    <div class="decor-field" role="img" aria-label="Decorative geometric pattern of blush facets with antique gold lines"></div>

    <div class="holder">
      <p class="holder-name"><strong>JAMES</strong> SMITH</p>
      <p class="holder-role">YOUR POSITION</p>
    </div>

    <ul class="contact-list">
      <li class="contact-item">
        <span>+(00) 123 4669</span>
        <svg class="contact-icon" viewBox="0 0 24 24" aria-hidden="true">
          <circle cx="12" cy="12" r="10"/>
          <path d="M8.5 7.5l2 -0.5 1 2.5 -1.3 1a6 6 0 0 0 2.8 2.8l1 -1.3 2.5 1 -0.5 2c-4.5 0.5 -8.5 -3.5 -8 -8z"/>
        </svg>
      </li>
      <li class="contact-item">
        <span>YOUR ADDRESS HERE</span>
        <svg class="contact-icon" viewBox="0 0 24 24" aria-hidden="true">
          <path d="M3 11l8 -7 8 7M5 9.5v10h7"/>
          <path d="M17 21s-4 -3.5 -4 -6.5a4 4 0 0 1 8 0c0 3 -4 6.5 -4 6.5z"/>
          <circle cx="17" cy="14.5" r="1.3"/>
        </svg>
      </li>
      <li class="contact-item">
        <span>YOUREMAIL@GMAIL.COM</span>
        <svg class="contact-icon" viewBox="0 0 24 24" aria-hidden="true">
          <circle cx="12" cy="12" r="10"/>
          <circle cx="12" cy="12" r="3"/>
          <path d="M15 9v4a2 2 0 0 0 4 0v-1a7 7 0 1 0 -3 5.7"/>
        </svg>
      </li>
      <li class="contact-item">
        <span>WWW.YOURWEBSITE.COM</span>
        <svg class="contact-icon" viewBox="0 0 24 24" aria-hidden="true">
          <circle cx="12" cy="12" r="9"/>
          <ellipse cx="12" cy="12" rx="4" ry="9"/>
          <path d="M3 12h18M4.5 7.5h15M4.5 16.5h15"/>
        </svg>
      </li>
    </ul>
  </section>

</main>
</body>
</html>
```